A comunicação apenas pelo chat ou com desenvolvedor que não se comunica com cliente é péssimo ! O desenvolvedor que não se comunica dificulta o desenvolvimento do trabalho causando uma demora ecessiva !

```html
<!DOCTYPE html>
<html lang="pt-BR">
<head>
<meta charset="utf-8">
<title>Envelope — Traçado Engenharia</title>
<link href="https://fonts.googleapis.com/css2?family=Montserrat:wght@400;500&display=swap" rel="stylesheet">
<style>
  :root {
    --canvas-bg: #e6e7e8;
    --paper: #ffffff;
    --band-gray: #c6c7c9;
    --ink: #141414;
    --ink-soft: #3a3a3a;
  }
  html, body {
    margin: 0;
    padding: 0;
    width: 1200px;
    height: 1200px;
    overflow: hidden;
    background: var(--canvas-bg);
  }
  .envelope-dieline {
    display: block;
    width: 1200px;
    height: 1200px;
    font-family: "Montserrat", sans-serif;
  }
  .paper { fill: var(--paper); }
  .band { fill: var(--band-gray); }
  .base { fill: var(--ink); }
  .brand-mark { fill: var(--ink); }
  .brand-name {
    fill: var(--ink);
    font-weight: 500;
    font-size: 25px;
    letter-spacing: 1.5px;
  }
  .contact-line {
    fill: var(--ink-soft);
    font-weight: 400;
    font-size: 11px;
    letter-spacing: 0.4px;
  }
  .contact-icon { fill: var(--ink); font-size: 10px; }
</style>
</head>
<body>
<svg class="envelope-dieline" viewBox="0 0 1200 1200" xmlns="http://www.w3.org/2000/svg">
  <!-- top flap -->
  <path class="paper top-flap" d="M192,150 Q196,104 250,96 L950,96 Q1004,104 1008,150 L1008,516 L192,516 Z"/>

  <!-- side flaps -->
  <path class="paper side-flap side-flap--left" d="M192,516 L150,524 Q125,530 125,560 L125,930 Q128,970 173,980 L192,876 Z"/>
  <path class="paper side-flap side-flap--right" d="M1008,516 L1050,524 Q1075,530 1075,560 L1075,930 Q1072,970 1027,980 L1008,876 Z"/>

  <!-- front panel -->
  <rect class="band front-panel" x="192" y="516" width="816" height="360"/>

  <!-- bottom flap -->
  <path class="base bottom-flap" d="M176,876 L1024,876 C1012,960 1004,1050 968,1080 Q956,1092 930,1092 L270,1092 Q244,1092 232,1080 C196,1050 188,960 176,876 Z"/>

  <!-- brand on top flap -->
  <g class="brand brand--flap">
    <rect class="brand-mark" x="232" y="422" width="50" height="50"/>
    <text class="brand-name" x="300" y="443">TRAÇADO</text>
    <text class="brand-name" x="300" y="472">ENGENHARIA</text>
  </g>

  <!-- front panel content, printed upside down -->
  <g class="front-content" transform="rotate(180 600 696)">
    <g class="brand brand--front">
      <rect class="brand-mark" x="412" y="632" width="50" height="50"/>
      <text class="brand-name" x="480" y="653">TRAÇADO</text>
      <text class="brand-name" x="480" y="682">ENGENHARIA</text>
    </g>
    <g class="contact-block">
      <text class="contact-line" x="600" y="808" text-anchor="middle"><tspan class="contact-icon">●</tspan><tspan dx="6">Endereço: Rua das Obras, 42</tspan></text>
      <text class="contact-line" x="600" y="828" text-anchor="middle"><tspan class="contact-icon">■</tspan><tspan dx="6">ola@tracado.com.br</tspan><tspan class="contact-icon" dx="16">●</tspan><tspan dx="6">www.tracado.com.br</tspan></text>
      <text class="contact-line" x="600" y="848" text-anchor="middle"><tspan class="contact-icon">●</tspan><tspan dx="6">+55 31 4000-1234</tspan><tspan class="contact-icon" dx="16">●</tspan><tspan dx="6">+55 31 4000-1234</tspan></text>
    </g>
  </g>
</svg>
</body>
</html>
```